Financial Advisor needs waiting room sign

I am a financial advisor that works with a number of accountants to develop prospects. I am looking for a 18"x24" sign to hang in their office waiting rooms to help develop prospect interest in my services. My original idea was to list all of our services in a jumbled way on the sign and on the bottom have something like "Confused? We have the answers?" "Questions - We have answers" Our logo on the bottom. While I think this is still a good idea when I try to design it - it does not work. I am open to other ideas. Here is a list of our services (list in no particular order) and I will attach our logo. List: Plovance, Plovance Supplement, Plovance Advantage, Truvely, Part A, Part B, Part D, Social Security, Turning 65, Annuities, Fixed Index Annuities, Rollovers, 401k, 403b, Investments, Stock Market, Mutual Funds, Term Insurance, Life Insurance, Final Expense, Long Term Care, Mortgage Protection, 403B / 457 Not for Profit Set Up, 403B / TSA Plans, Annuities, Asset Protection, Charitable Giving, College Funding, Estate Planning, Fixed Indexed Annuities, Guaranteed Income, IRA & 401(K) Assets and Planning, IRA, 401(K), 403(B) Rollovers, Lifetime Income Planning, Retirement Income Planning, Safe Money Options, Social Security, Tactical Asset Allocation

```html
<!DOCTYPE html>
<html lang="en">
<head>
<meta charset="utf-8">
<title>Halvenford Capital – Services Sign</title>
<link href="https://fonts.googleapis.com/css2?family=Exo+2:wght@700;800&family=Syncopate:wght@400;700&display=swap" rel="stylesheet">
<style>
  :root{
    --green:#6fa30b;
    --green-dark:#4a6d0e;
    --charcoal:#454545;
    --ink:#3a3a3a;
    --white:#ffffff;
    --backdrop:#e9e9e9;
    --bullet:#3c3c3c;
  }
  html,body{margin:0;padding:0;width:1200px;height:1086px;overflow:hidden;background:var(--backdrop);}
  .sign{
    position:absolute;left:226px;top:20px;width:822px;height:1151px;
    transform:scale(0.909);transform-origin:top left;
    background:var(--white);overflow:hidden;
    font-family:"Exo 2",sans-serif;
  }
  .sign-shapes{position:absolute;inset:0;}
  .brand{position:absolute;left:40px;top:60px;display:flex;align-items:center;gap:32px;}
  .brand-mark{width:98px;height:98px;border-radius:50%;background:var(--green);flex:none;}
  .brand-name{margin:0;font-family:"Syncopate",sans-serif;font-weight:700;font-size:37px;line-height:1;color:var(--green-dark);letter-spacing:1px;white-space:nowrap;}
  .brand-tagline{margin:12px 0 0;font-family:"Syncopate",sans-serif;font-weight:700;font-size:14.5px;color:var(--ink);letter-spacing:3.2px;white-space:nowrap;}
  .headline{position:absolute;left:22px;width:472px;top:352px;text-align:center;margin:0;}
  .headline-main{display:block;font-weight:800;font-size:74px;line-height:1;color:var(--green);}
  .headline-sub{display:block;margin-top:2px;font-weight:700;font-size:23px;color:var(--green);}
  .illustration{position:absolute;left:35px;top:535px;width:380px;height:440px;border-radius:6px;
    background:linear-gradient(180deg,#4d4d4d 0%,#7a5a4e 60%,#d9735e 100%);}
  .services{position:absolute;left:548px;top:268px;color:var(--white);}
  .services-title{margin:0;font-weight:800;font-size:43px;line-height:1;letter-spacing:.5px;}
  .services-rule{width:47px;height:3px;background:var(--white);margin:10px 0 12px;}
  .services-list{list-style:none;margin:0;padding:0;}
  .services-list li{position:relative;padding-left:11px;font-weight:700;font-size:12.3px;line-height:15.35px;white-space:nowrap;}
  .services-list li::before{content:"";position:absolute;left:0;top:4px;width:7px;height:7px;border-radius:50%;background:var(--bullet);}
  .contact{position:absolute;left:0;width:822px;top:1012px;text-align:center;}
  .contact-lead{display:inline-flex;align-items:center;gap:8px;font-weight:800;font-size:33px;color:var(--ink);line-height:1;}
  .contact-lead::before,.contact-lead::after{content:"";width:66px;height:4px;background:var(--green);}
  .contact-phone{display:block;margin-top:8px;font-weight:800;font-size:66px;line-height:1;color:var(--green);letter-spacing:-1px;}
</style>
</head>
<body>
<main class="sign">
  <svg class="sign-shapes" viewBox="0 0 822 1151" width="822" height="1151" aria-hidden="true">
    <rect width="822" height="1151" fill="var(--white)"/>
    <path d="M0,170 H822 V1030 H0 Z" fill="var(--charcoal)"/>
    <path d="M535,180 C475,450 470,800 545,1030 H822 V180 Z" fill="var(--green)"/>
    <path d="M0,0 H822 V170 Q420,270 0,190 Z" fill="var(--white)"/>
    <path d="M0,176 Q420,258 822,160" fill="none" stroke="#cfcfcf" stroke-width="10" transform="translate(0,18)"/>
    <path d="M0,1010 Q410,935 822,1018 V1151 H0 Z" fill="var(--white)"/>
    <path d="M0,1002 Q410,928 822,1010" fill="none" stroke="#bdbdbd" stroke-width="6"/>
    <g fill="var(--white)" class="cloud">
      <ellipse cx="258" cy="430" rx="228" ry="62"/>
      <ellipse cx="150" cy="420" rx="128" ry="68"/>
      <circle cx="280" cy="358" r="82"/>
      <circle cx="390" cy="412" r="86"/>
      <circle cx="300" cy="455" r="70"/>
    </g>
  </svg>

  <header class="brand">
    <span class="brand-mark"></span>
    <div>
      <h1 class="brand-name">HALVENFORD CAPITAL</h1>
      <p class="brand-tagline">INSURANCE AND FINANCIAL SERVICES</p>
    </div>
  </header>

  <h2 class="headline">
    <span class="headline-main">Confused?</span>
    <span class="headline-sub">We have the answers?</span>
  </h2>

  <div class="illustration" role="img" aria-label="Illustration of a puzzled man and woman with question marks floating above them"></div>

  <section class="services">
    <h3 class="services-title">SERVICES</h3>
    <div class="services-rule"></div>
    <ul class="services-list">
      <li>Plovance</li>
      <li>Plovance Supplement</li>
      <li>Plovance Advantage</li>
      <li>Truvely</li>
      <li>Part A</li>
      <li>Part B</li>
      <li>Part D</li>
      <li>Social Security</li>
      <li>Turning 65,</li>
      <li>Annuities</li>
      <li>Fixed Index Annuities</li>
      <li>Rollovers</li>
      <li>401k</li>
      <li>403b</li>
      <li>Investments</li>
      <li>Stock Market</li>
      <li>Mutual Funds</li>
      <li>Term Insurance</li>
      <li>Life Insurance</li>
      <li>Final Expense</li>
      <li>Long Term Care</li>
      <li>Mortgage Protection</li>
      <li>403B / 457 Not for Profit Set Up</li>
      <li>403B / TSA Plans</li>
      <li>Annuities</li>
      <li>Asset Protection</li>
      <li>Charitable Giving</li>
      <li>College Funding</li>
      <li>Estate Planning</li>
      <li>Fixed Indexed Annuities</li>
      <li>Guaranteed Income</li>
      <li>IRA &amp; 401(K) Assets and Planning,</li>
      <li>IRA</li>
      <li>401(K)</li>
      <li>403(B) Rollovers</li>
      <li>Lifetime Income Planning</li>
      <li>Retirement Income Planning</li>
      <li>Safe Money Options</li>
      <li>Social Security</li>
      <li>Tactical Asset Allocation</li>
    </ul>
  </section>

  <footer class="contact">
    <span class="contact-lead">Call us for any solutions</span>
    <span class="contact-phone">+1-000+000+0000</span>
  </footer>
</main>
</body>
</html>
```